Building Servicess

We need a new business card design for a company. We specialise in: Electrical/Site temporary electrics, Data/Network Installation, Passive Fire Protection

Industry/Entity Type

Construction

Contact Information for Business Card

Services provided as detailed on project description

Font styles to use
Serif

Colors
0054AA
0677BA
7BADD7
CADEEF
E8F1F8
00AB8E
00BBA5
67D7C9
C6EFE9
E9F9F6
EB3D1F
EC4F4E
F09395
F8D3D4
FCEDEE

Requirements
Must have
• Company logo-contact details-phone numbers

```html
<!DOCTYPE html>
<html lang="en">
<head>
<meta charset="utf-8">
<title>Northbay Building Services – Business Card</title>
<link href="https://fonts.googleapis.com/css2?family=Montserrat:wght@500;700&family=Poppins:wght@300;400&display=swap" rel="stylesheet">
<style>
  :root {
    --brand-blue: #1469a9;
    --brand-grey: #6d6e71;
    --text-grey: #4a4a4a;
    --card-white: #f7f7f5;
    --backdrop: #e4e4e1;
  }
  * { box-sizing: border-box; margin: 0; padding: 0; }
  html, body { width: 1200px; height: 801px; overflow: hidden; }
  body {
    background: var(--backdrop);
    position: relative;
    font-family: "Poppins", sans-serif;
  }
  .card {
    position: absolute;
    top: 252px;
    width: 520px;
    height: 297px;
    box-shadow: 0 10px 28px rgba(0,0,0,0.14);
    overflow: hidden;
  }
  .card--front { left: 50px; background: var(--card-white); }
  .card--back  { left: 630px; background: var(--brand-blue); }

  .front__band {
    position: absolute;
    left: 0; top: 22px;
    width: 170px; height: 46px;
    background: var(--brand-blue);
  }
  .brand {
    position: absolute;
    font-family: "Montserrat", sans-serif;
    font-weight: 700;
    color: var(--brand-blue);
    text-transform: uppercase;
  }
  .brand__row { display: flex; align-items: center; gap: 8px; }
  .brand__mark { width: 14px; height: 14px; background: currentColor; flex: none; }
  .brand__name { font-size: 17px; letter-spacing: 0.5px; white-space: nowrap; }
  .brand__rule { height: 1.5px; background: var(--brand-grey); margin-top: 4px; }
  .brand__suffix {
    font-family: "Montserrat", sans-serif;
    font-weight: 500; font-size: 8px; letter-spacing: 4px;
    text-align: right; margin-top: 2px; color: var(--brand-grey);
  }
  .card--front .brand { left: 182px; top: 30px; }

  .holder { position: absolute; left: 300px; top: 128px; }
  .holder__name {
    font-family: "Montserrat", sans-serif;
    font-weight: 700; font-size: 20px; color: var(--brand-blue);
    letter-spacing: 0.5px; text-transform: uppercase;
  }
  .holder__role { font-size: 12px; font-weight: 300; color: var(--text-grey); margin-top: 2px; padding-left: 40px; }

  .contact { position: absolute; left: 120px; top: 184px; list-style: none; }
  .contact li {
    display: flex; align-items: flex-start; gap: 8px;
    font-size: 11px; font-weight: 300; color: var(--text-grey); line-height: 16px;
  }
  .contact li + li { margin-top: 2px; }
  .contact svg { width: 11px; height: 11px; margin-top: 2px; flex: none; fill: var(--brand-blue); }
  .contact .address { margin-bottom: 8px; }

  .card--back .brand {
    left: 50%; top: 50%; transform: translate(-50%, -50%);
    color: #fff;
  }
  .card--back .brand__name { font-size: 24px; }
  .card--back .brand__mark { width: 18px; height: 18px; }
  .card--back .brand__rule { background: #fff; }
  .card--back .brand__suffix { color: #fff; font-size: 9px; }
</style>
</head>
<body>
  <section class="card card--front" aria-label="Business card front">
    <div class="front__band"></div>
    <div class="brand">
      <div class="brand__row"><span class="brand__mark"></span><span class="brand__name">Northbay Building Services</span></div>
      <div class="brand__rule"></div>
      <div class="brand__suffix">Ltd</div>
    </div>

    <div class="holder">
      <p class="holder__name">Daniel Rowe</p>
      <p class="holder__role">Managing Director</p>
    </div>

    <ul class="contact">
      <li class="address">
        <svg viewBox="0 0 12 12"><path d="M6 0.5a4 4 0 0 0-4 4c0 3 4 7 4 7s4-4 4-7a4 4 0 0 0-4-4zm0 5.6a1.6 1.6 0 1 1 0-3.2 1.6 1.6 0 0 1 0 3.2z"/></svg>
        <span>14 Harbour Road, Unit 3<br>Leeds, LS1 4AB, UK</span>
      </li>
      <li>
        <svg viewBox="0 0 12 12"><path d="M2.5 1h2l1 2.6-1.3 1a6.5 6.5 0 0 0 3.2 3.2l1-1.3 2.6 1v2a1 1 0 0 1-1 1A9.5 9.5 0 0 1 1.5 2a1 1 0 0 1 1-1z"/></svg>
        <span>(555) 014-2290</span>
      </li>
      <li>
        <svg viewBox="0 0 12 12"><path d="M1 2.5h10v7H1z M1 2.5l5 4 5-4" stroke="#fff" stroke-width="0.8"/></svg>
        <span>hello@northbaybuild.co</span>
      </li>
      <li>
        <svg viewBox="0 0 12 12"><circle cx="6" cy="6" r="5"/><path d="M1 6h10M6 1c-2 2.7-2 7.3 0 10M6 1c2 2.7 2 7.3 0 10" stroke="#fff" stroke-width="0.7" fill="none"/></svg>
        <span>www.northbaybuild.co</span>
      </li>
    </ul>
  </section>

  <section class="card card--back" aria-label="Business card back">
    <div class="brand">
      <div class="brand__row"><span class="brand__mark"></span><span class="brand__name">Northbay Building Services</span></div>
      <div class="brand__rule"></div>
      <div class="brand__suffix">Ltd</div>
    </div>
  </section>
</body>
</html>
```